ROBERTO VENTRANZI and his Orchestra "Under The Lanterns"

Music event. Friday November 6, 2015. Doors open 7pm
Venue - The Harwell Lane Hall, 47 Dunmore Rd. Perth. WA. 6000.
Roberto and his 12 piece band will perform inside a boxing ring in a very funky viby venue "The Harwell Lane Hall" in Perth, WA. The venue is a gorgeous retro looking place. See pics attached.
This "live music" event is focused on Roberto Ventranzi - with a twist. The 12 piece band and Roberto will be performing in the boxing ring - a really cool and quirky concept.
The whole event will be filmed and recorded - to make a DVD.
Updates

please don't focus on boxing this is a music event - the 11 piece band will perform in the boxing ring doesn't need to look "tough guy"

Target Market(s)

music lovers - 35 to 70. It needs to feel funky but still elegant focus to a mature fun loving audience "who have seen it all before".
Glitterati and Media event. Food lovers.....Tavolino Event Catering to provide italian tapas food included in the ticket price from 7pm to 8:30pm .....also includes 2 complimentary drinks

Industry/Entity Type

Gym

Font styles to use
Sans Serif

Requirements
Must have
• A powerful focus on Roberto Ventranzi and his band . . . and his music.
• A "wow factor" of it being "Under The Lanterns" a totally new concept in Perth nightlife entertainment. Basically, the boxing ring is the stage. ALSO, please mention that this event will be filmed with 8 cameras and digitally recorded. A 5.1 surround sound DVD will be made of this event . . . and we want "you" (the people) to be a part of it. And we'll have cameramen going through the crowd interviewing everyone for the "behind the scenes" section of the DVD. This is a super-exclusive event. Only 150 tix available - so get in quick.
Nice to have
• Included in the ticket price of $100 is 2 complimentary drinks (beer/wine/bubbly) and lots of delicious italian tapas food from 7pm to 8:30pm - provided by Tavolino Events Catering. Extra drinks including spirits and cocktails can be purchased at the bar. Show starts at 8:30pm sharp.
Should not have
• no typical Italian anything please

```html
<!DOCTYPE html>
<html lang="en">
<head>
<meta charset="utf-8">
<title>Roberto Ventranzi and His Orchestra – Under The Lanterns</title>
<link rel="stylesheet" href="https://fonts.googleapis.com/css2?family=Oswald:wght@400;500;700&family=Anton&family=Open+Sans:wght@400;600&display=swap">
<style>
  :root {
    --ink: #141414;
    --white: #ffffff;
    --smoke-dark: #2b2b2b;
    --smoke-mid: #5c5c5c;
    --smoke-light: #8d8d8d;
    --stage-dark: #101010;
    --stage-mid: #2e2e2e;
    --paper: #e4e4e4;
    --paper-light: #f6f6f6;
    --shadow: rgba(0,0,0,0.75);
  }
  * { margin: 0; padding: 0; box-sizing: border-box; }
  html, body { width: 816px; height: 1200px; overflow: hidden; background: var(--paper); }
  .poster { position: relative; width: 816px; height: 1200px; overflow: hidden; background: linear-gradient(180deg, var(--paper) 0%, var(--paper-light) 100%); font-family: 'Oswald', sans-serif; color: var(--white); }

  .venue-photo { position: absolute; left: 0; top: 0; width: 816px; height: 580px;
    background: linear-gradient(160deg, var(--smoke-dark) 0%, var(--smoke-mid) 30%, var(--smoke-light) 55%, var(--smoke-mid) 80%, var(--smoke-dark) 100%); }
  .venue-photo::after { content: ""; position: absolute; left: 0; top: 0; width: 100%; height: 110px; background: linear-gradient(180deg, rgba(0,0,0,0.55), rgba(0,0,0,0)); }

  .event-details { position: absolute; top: 14px; left: 0; width: 816px; text-align: center; font-family: 'Oswald', sans-serif; font-weight: 700; letter-spacing: 1px; text-shadow: 2px 2px 3px var(--shadow); z-index: 2; }
  .event-date { font-size: 30px; line-height: 36px; }
  .event-venue { font-size: 27px; line-height: 34px; }

  .headline { position: absolute; left: 70px; top: 190px; width: 700px; text-align: center; transform: rotate(-4deg); transform-origin: center; font-family: 'Anton', sans-serif; text-transform: uppercase; letter-spacing: 2px; z-index: 2;
    text-shadow: 3px 3px 0 var(--ink), -1px -1px 0 var(--ink), 1px -1px 0 var(--ink), -1px 1px 0 var(--ink), 4px 6px 8px var(--shadow); }
  .headline-name { font-size: 84px; line-height: 92px; }
  .headline-band { font-size: 46px; line-height: 50px; }
  .headline-title { font-size: 78px; line-height: 88px; }

  .stage-band { position: absolute; left: 0; top: 0; width: 816px; height: 1200px;
    clip-path: polygon(0 540px, 816px 470px, 816px 905px, 0 955px);
    background: radial-gradient(ellipse at 30% 55%, var(--stage-mid) 0%, var(--stage-dark) 70%); }

  .portrait { position: absolute; left: 570px; top: 560px; width: 246px; height: 330px;
    background: linear-gradient(180deg, #4a4a4a 0%, #7a7a7a 40%, #2a2a2a 100%); }

  .invitation { position: absolute; left: 120px; top: 600px; width: 440px; text-align: center; transform: rotate(-4deg); font-family: 'Oswald', sans-serif; font-weight: 700; text-transform: uppercase; text-shadow: 2px 2px 3px var(--shadow); }
  .invitation-join { font-size: 44px; line-height: 46px; }
  .invitation-name { font-size: 38px; line-height: 42px; }
  .invitation-ring { font-size: 30px; line-height: 36px; margin-bottom: 12px; }
  .invitation-line { font-size: 21px; line-height: 25px; font-weight: 500; }

  .crowd-note { position: absolute; left: 40px; top: 985px; width: 736px; text-align: center; font-family: 'Open Sans', sans-serif; font-size: 15px; line-height: 22px; color: var(--ink); }
  .crowd-note strong { font-weight: 600; }

  .catering { position: absolute; left: 30px; top: 1085px; width: 756px; display: flex; align-items: center; gap: 18px; color: var(--ink); }
  .caterer-mark { display: flex; align-items: center; gap: 8px; flex: 0 0 auto; }
  .caterer-square { width: 40px; height: 40px; background: var(--ink); }
  .caterer-name { font-family: 'Open Sans', sans-serif; font-size: 14px; font-weight: 600; color: var(--ink); }
  .catering-terms { font-family: 'Open Sans', sans-serif; font-size: 12px; line-height: 17px; text-align: center; }
</style>
</head>
<body>
<main class="poster">
  <div class="venue-photo" role="img" aria-label="Interior of The Harwell Lane Hall with vintage signage and warm retro fittings"></div>

  <header class="event-details">
    <p class="event-date">NOVEMBER 6, 2015. 7PM</p>
    <p class="event-venue">THE HARWELL LANE HALL, 47 DUNMORE RD. PERTH. WA. 6000.</p>
  </header>

  <h1 class="headline">
    <span class="headline-name" style="display:block">Roberto Ventranzi</span>
    <span class="headline-band" style="display:block">And His Orchestra</span>
    <span class="headline-title" style="display:block">"Under The Lanterns"</span>
  </h1>

  <div class="stage-band" role="img" aria-label="Orchestra performing on a boxing ring stage under low lights"></div>
  <div class="portrait" role="img" aria-label="Portrait of the singer Roberto Ventranzi"></div>

  <section class="invitation">
    <p class="invitation-join">Join</p>
    <p class="invitation-name">Roberto and his orchestra</p>
    <p class="invitation-ring">who will jam in a boxing ring!</p>
    <p class="invitation-line">This event will be filmed with 8 cameras</p>
    <p class="invitation-line">and digitally recorded.</p>
    <p class="invitation-line">To be made into a DVD.</p>
    <p class="invitation-line">This is a super exclusive event</p>
    <p class="invitation-line">and we want you to be a part of it!</p>
  </section>

  <p class="crowd-note">We'll have cameramen going through the crowd interviewing everyone for the "behind the scenes" section of the DVD.<br><strong>Only 150 tickets available, so get in quick!</strong></p>

  <footer class="catering">
    <div class="caterer-mark">
      <span class="caterer-square"></span>
      <span class="caterer-name">Tavolino</span>
    </div>
    <p class="catering-terms">Included in the ticket price of $100 is 2 complimentary drinks and lots of delicious Italian tapas food from 7pm to 8:30pm provided by Tavolino Events Catering. Extra drinks including spirits and cocktails can be purchased at the bar. Show starts at 8:30pm sharp.</p>
  </footer>
</main>
</body>
</html>
```